Distribution company for alcoholic beverages called Amber Ledger needs a web design

1. We would like to first page to show

A. The company logo (in att)

B. A wall of bottles similar to
- www.tallcaskhollow.com that will click through to the brand info
- https://velmarcellars.com/brands/
PLEASE NOTE THAT IT CAN NOT BE THE SAME DESIGN - it needs to have a different look and feel ... this is to show what we mean with a wall of bottles

Important = we need to be able to keep adding new bottles/brands over time

C. only 3 tabs needed – Brands, About Us and Contact

Style
- simple and clean
- colourful
- classy

2. Page 2
The intro page to describe the company
we can use the same (Box + drop) logo to create a visual

3. Page 3
The referral page to the specific brands/company
= we need to alternating versions of this / just different ordering in the page

Target Market(s)

importers, brand owners, bartenders,

Industry/Entity Type

It Company

Number of Pages Required

3 page

Requirements
Must have
• A landing page visual that can display bottles we will sell in an organised way
• We need to be able to add bottles when the portfolio expands
Nice to have
• to have the drop out of the logo as a part of the design of the website

```html
<!DOCTYPE html>
<html lang="en">
<head>
<meta charset="utf-8">
<title>Amber Ledger — Wine Bottle</title>
<link href="https://fonts.googleapis.com/css2?family=Montserrat:wght@400;500;600;700;800&display=swap" rel="stylesheet">
<style>
  :root {
    --crimson: #ad1b3c;
    --crimson-dark: #8f1430;
    --ink: #1e1e22;
    --ink-soft: #3a3a3f;
    --muted: #8a8a90;
    --page: #ffffff;
    --stage: #f1f1f3;
    --stage-light: #fafafb;
    --white: #ffffff;
  }
  * { box-sizing: border-box; margin: 0; padding: 0; }
  html, body {
    width: 1200px; height: 600px; overflow: hidden;
    background: var(--page);
    font-family: "Montserrat", sans-serif;
    color: var(--ink);
  }
  a { text-decoration: none; }
  .site {
    position: absolute; left: 99px; top: 0;
    width: 1003px; height: 600px;
    background: radial-gradient(ellipse at 50% 45%, var(--stage-light) 0%, var(--stage) 70%, #e9e9ec 100%);
    box-shadow: 0 0 40px rgba(0,0,0,0.12);
    overflow: hidden;
  }
  /* Header */
  .header {
    position: absolute; left: 0; top: 0; width: 100%; height: 60px;
    background: var(--crimson); color: var(--white);
  }
  .brand-name {
    position: absolute; left: 43px; top: 15px; width: 109px; height: 30px;
    display: flex; align-items: center; justify-content: center; gap: 5px;
    font-weight: 700; font-size: 9.5px; letter-spacing: 0.4px; text-transform: uppercase;
    white-space: nowrap;
    border: 1px solid rgba(255,255,255,0.85);
  }
  .brand-dot { width: 5px; height: 5px; border-radius: 50%; background: var(--white); flex: none; }
  .contact-item {
    position: absolute; top: 22px; display: flex; align-items: center; gap: 7px;
    font-size: 12px; font-weight: 600; white-space: nowrap;
  }
  .contact-email { left: 171px; }
  .contact-phone { left: 353px; }
  .nav { position: absolute; right: 42px; top: 22px; display: flex; gap: 25px; }
  .nav a { color: var(--white); font-size: 12px; font-weight: 700; letter-spacing: 0.3px; }

  /* Product hero */
  .title-ghost, .title {
    position: absolute; font-weight: 800; font-size: 74px; letter-spacing: -1px; line-height: 1;
    white-space: nowrap;
  }
  .title-ghost { left: 190px; top: 62px; color: rgba(0,0,0,0.06); }
  .title { left: 170px; top: 80px; color: var(--crimson); }
  .title-rule { position: absolute; left: 172px; top: 170px; width: 451px; height: 1px; background: var(--crimson); }

  .bottle-hero {
    position: absolute; left: 456px; top: 124px; width: 92px; height: 374px;
    border-radius: 10px 10px 14px 14px;
    background: linear-gradient(90deg, #2a1a20 0%, #4a3038 45%, #2c1c22 100%);
  }
  .bottle-shadow {
    position: absolute; left: 440px; top: 492px; width: 124px; height: 16px;
    border-radius: 50%; background: radial-gradient(ellipse, rgba(0,0,0,0.18), rgba(0,0,0,0) 70%);
  }

  .description {
    position: absolute; left: 172px; top: 214px;
    font-size: 10.3px; line-height: 12.4px; color: var(--ink-soft); font-weight: 500;
    white-space: nowrap;
  }
  .specs { position: absolute; left: 172px; top: 314px; font-size: 11.5px; line-height: 14.5px; }
  .spec-row { display: flex; }
  .spec-row dt { width: 125px; font-weight: 700; color: var(--ink); }
  .spec-row dd { color: var(--ink-soft); font-weight: 500; }

  .btn-buy {
    position: absolute; left: 172px; top: 396px; width: 129px; height: 43px;
    background: var(--crimson); color: var(--white);
    display: flex; align-items: center; justify-content: center; gap: 7px;
    font-size: 12px; font-weight: 700; box-shadow: 0 6px 14px rgba(173,27,60,0.25);
  }
  .link-more {
    position: absolute; left: 318px; top: 411px;
    color: var(--crimson); font-size: 10.5px; font-weight: 700; text-decoration: underline;
  }

  /* Bottle wall */
  .pager { position: absolute; left: 593px; top: 215px; display: flex; align-items: center; gap: 6px; font-size: 11px; font-weight: 500; }
  .pager-count { margin-right: 3px; }
  .pager-btn {
    width: 13px; height: 12px; background: var(--crimson); color: var(--white);
    font-size: 8px; display: flex; align-items: center; justify-content: center; border-radius: 1px;
  }
  .thumb-card {
    position: absolute; top: 244px; width: 111px; height: 206px;
    background: var(--white); box-shadow: 0 6px 18px rgba(0,0,0,0.08);
  }
  .thumb-first { left: 594px; }
  .thumb-second { left: 740px; }
  .thumb-bottle {
    position: absolute; left: 43px; top: 40px; width: 25px; height: 114px; border-radius: 4px;
    background: linear-gradient(180deg, #c8304f 0%, #c8304f 10%, #2c1c22 14%, #3c2830 100%);
  }

  /* Bottom switcher */
  .switcher { position: absolute; left: 0; top: 523px; width: 100%; height: 77px; }
  .switch-panel {
    position: absolute; top: 0; width: 257px; height: 77px; background: var(--crimson); color: var(--white);
  }
  .switch-prev { left: 0; }
  .switch-next { right: 0; }
  .switch-label { position: absolute; top: 24px; font-size: 11px; font-weight: 500; opacity: 0.85; white-space: nowrap; }
  .switch-name { position: absolute; top: 39px; font-size: 15.5px; font-weight: 700; white-space: nowrap; }
  .switch-prev .switch-label, .switch-prev .switch-name { right: 70px; text-align: right; }
  .switch-next .switch-label, .switch-next .switch-name { left: 87px; }
  .switch-arrow { position: absolute; top: 30px; }
  .switch-prev .switch-arrow { left: 25px; }
  .switch-next .switch-arrow { right: 25px; }
  .switch-thumb { position: absolute; top: 6px; width: 20px; height: 66px; border-radius: 4px; }
  .switch-prev .switch-thumb { right: 34px; background: linear-gradient(180deg, #2a6fb8, #0e2b55); }
  .switch-next .switch-thumb { left: 50px; background: linear-gradient(180deg, #3a2a10, #c88a1c 60%, #5a3a08); }
  .switch-active {
    position: absolute; left: 257px; top: 0; width: 489px; height: 77px;
    background: rgba(255,255,255,0.55); text-align: center;
  }
  .switch-active .switch-label { position: static; display: block; margin-top: 24px; color: var(--muted); opacity: 1; }
  .switch-active .switch-name { position: static; display: block; margin-top: 3px; color: var(--ink); }
</style>
</head>
<body>
<div class="site">
  <header class="header">
    <div class="brand-name"><span class="brand-dot"></span>Amber Ledger</div>
    <div class="contact-item contact-email">
      <svg width="11" height="9" viewBox="0 0 11 9"><rect width="11" height="9" rx="1" fill="#fff"/><path d="M0.5 1 L5.5 5 L10.5 1" stroke="#ad1b3c" stroke-width="1.2" fill="none"/></svg>
      hello@amberledger.com
    </div>
    <div class="contact-item contact-phone">
      <svg width="10" height="10" viewBox="0 0 10 10"><path d="M2 0.5 L3.6 2.8 L2.7 4 Q4 6.3 6 7.3 L7.2 6.4 L9.5 8 L8.4 9.5 Q3.5 9 0.5 1.6 Z" fill="#fff"/></svg>
      +380441230987
    </div>
    <nav class="nav">
      <a href="#">BRAND</a>
      <a href="#">ABOUT US</a>
      <a href="#">CONTACT</a>
    </nav>
  </header>

  <div class="title-ghost" aria-hidden="true">Wine Bottle</div>
  <h1 class="title">Wine Bottle</h1>
  <div class="title-rule"></div>

  <div class="bottle-shadow"></div>
  <div class="bottle-hero" role="img" aria-label="Photograph of a dark red wine bottle with a pink capsule and black label"></div>

  <p class="description">A wine bottle made especially for using it in<br>Photoshop presentations. This bottle<br>does not need unnecessary comments.<br>Look at its forms, its rustled glass of glass<br>and you will immediately have a desire to<br>buy it (if we sell it). Lovely bottle in fine work.<br>Nothing more.</p>

  <dl class="specs">
    <div class="spec-row"><dt>Color:</dt><dd>Pink</dd></div>
    <div class="spec-row"><dt>Years:</dt><dd>2013-2018</dd></div>
    <div class="spec-row"><dt>Made in:</dt><dd>Francia</dd></div>
  </dl>

  <a class="btn-buy" href="#">BUY THIS
    <svg width="11" height="10" viewBox="0 0 11 10"><path d="M0 0.5 H2 L3.2 6.5 H9.3 L10.5 2 H2.6" fill="#fff" stroke="#fff" stroke-width="0.8"/><circle cx="4" cy="8.6" r="1" fill="#fff"/><circle cx="8.5" cy="8.6" r="1" fill="#fff"/></svg>
  </a>
  <a class="link-more" href="#">READ MORE</a>

  <div class="pager">
    <span class="pager-count">1/4</span>
    <span class="pager-btn">&lt;</span>
    <span class="pager-btn">&gt;</span>
  </div>
  <div class="thumb-card thumb-first"><div class="thumb-bottle" role="img" aria-label="Front view of the wine bottle"></div></div>
  <div class="thumb-card thumb-second"><div class="thumb-bottle" role="img" aria-label="Alternate view of the wine bottle"></div></div>

  <div class="switcher">
    <a class="switch-panel switch-prev" href="#">
      <svg class="switch-arrow" width="18" height="14" viewBox="0 0 18 14"><path d="M17 7 H2 M7 1 L1 7 L7 13" stroke="#fff" stroke-width="1.6" fill="none"/></svg>
      <span class="switch-label">Prev bottle:</span>
      <span class="switch-name">Whiskey 1998</span>
      <span class="switch-thumb" role="img" aria-label="Blue whiskey bottle"></span>
    </a>
    <div class="switch-active">
      <span class="switch-label">Active bottle:</span>
      <span class="switch-name">Whine Bottle</span>
    </div>
    <a class="switch-panel switch-next" href="#">
      <span class="switch-thumb" role="img" aria-label="Amber whiskey bottle"></span>
      <span class="switch-label">Next bottle:</span>
      <span class="switch-name">Whiskey 1999</span>
      <svg class="switch-arrow" width="18" height="14" viewBox="0 0 18 14"><path d="M1 7 H16 M11 1 L17 7 L11 13" stroke="#fff" stroke-width="1.6" fill="none"/></svg>
    </a>
  </div>
</div>
</body>
</html>
```